Roles For Metrics - Job Board for Big Data Professionals

Hi all,

I need a design for a job board I'm kicking off that is focused on finding jobs and people that work in Data Analytics.

I've attached a fairly in depth design spec and wireframe giving a rough mockup. Please note that in the wireframe, the boxes are there to demonstrate orders of content. This is not to say that a lot of distinct content boxes will necessarily be the best way of presenting content.

I will be available on Chatterlink (marcus.wendholt) and email (w3ndh0lt@quillpost.net) and will give constant and clear feedback on the way.

Payment is not guaranteed yet. As soon as there are at least 5+ promising designs I will make this guaranteed.

Thanks
Marcus
Updates

Hi all

Please suspend all work on this project for the time being.

I am working closely with 1 designer who I will very likely accept their design.

I appreciate all the work you have put into this, but dont want to waste any more of your time.

Thanks
Marcus

Industry/Entity Type

Work

Requirements
Must have
• I'd like a clean, modern web design which has strong use of Typography. Strong use of a clear and consistent palette of colours.
Should not have
• Boxes with rounded edges

```html
<!DOCTYPE html>
<html lang="en">
<head>
<meta charset="utf-8">
<title>Wendholt – Roles For Metrics Job Board</title>
<link href="https://fonts.googleapis.com/css2?family=Source+Sans+3:wght@400;600;700&display=swap" rel="stylesheet">
<style>
:root{
  --blue:#1189d6;
  --blue-dark:#0b6fb4;
  --blue-pale:#d3ebf9;
  --blue-line:#5fb3e6;
  --yellow:#fcc51d;
  --yellow-light:#ffe27a;
  --orange:#f26a2b;
  --black:#111;
  --ink:#333;
  --grey:#666;
  --link:#2b7bb9;
  --footer:#124f7e;
  --footer-dark:#0c3a61;
  --white:#fff;
}
*{box-sizing:border-box;margin:0;padding:0}
html,body{width:868px;height:1200px;overflow:hidden}
body{position:relative;background:var(--white);font-family:"Source Sans 3",sans-serif;color:var(--ink);font-size:11px}
.abs{position:absolute}
a{color:inherit;text-decoration:none}

.topbar{left:0;top:0;width:868px;height:18px;background:var(--black);color:#fff;font-size:10px;text-align:right;padding:3px 62px 0 0}
.brand{left:32px;top:38px}
.brand-name{font-size:32px;font-weight:700;color:var(--blue);line-height:1}
.brand-tag{font-size:12px;color:var(--blue);margin-top:1px}
.promo{left:393px;top:42px;width:434px;height:50px;background:#eaf4fb;border:1px solid #9ccbe9;display:flex;align-items:center;padding:0 8px}
.promo-q{font-weight:700;font-size:13px;line-height:1;color:#111;text-align:center;width:100px}
.promo-seal{width:40px;height:40px;border-radius:50%;background:#d8202a;color:#fff;font-size:8px;font-weight:700;text-align:center;display:flex;align-items:center;justify-content:center;line-height:1;margin:0 4px}
.promo-cta{flex:1;background:var(--yellow);border:1px solid #d89c00;font-weight:700;font-size:13px;color:#111;padding:5px 6px}

.nav{left:0;top:108px;width:868px;height:29px;background:var(--blue);display:flex;padding-left:32px}
.nav a{color:#fff;font-size:13px;padding:6px 17px 0;border-right:1px solid #3aa0e0;height:29px}
.nav a.active{background:var(--blue-pale);color:var(--blue-dark)}
.subnav{left:0;top:137px;width:868px;height:27px;background:var(--blue-pale);color:var(--blue-dark);font-size:12px;padding:6px 0 0 105px}

.box{border:1px solid var(--blue-line);background:#fff}
.head-yellow{height:27px;background:var(--yellow);font-size:15px;color:#222;display:flex;align-items:center;padding-left:8px;gap:6px}
.head-black{height:27px;background:var(--black);color:#fff;font-size:15px;padding:5px 14px}
.field{height:19px;border:1px solid #bbb;background:#fff;font-size:10px;color:#999;padding:2px 6px}
.btn{background:var(--blue);color:#fff;display:inline-block}

.signin{left:20px;top:177px;width:386px;height:159px}
.label{font-size:14px;color:#111}
.quick{left:20px;top:342px;width:386px;height:190px;background:linear-gradient(var(--yellow-light),var(--yellow));box-shadow:0 4px 6px rgba(0,0,0,.2)}
.quick .label{position:absolute;left:16px;font-size:15px;color:#4a3a00}
.check{display:inline-block;width:10px;height:10px;border:1px solid #999;background:#fff;vertical-align:-1px;margin-right:5px}

h2.section{font-size:17px;font-weight:400;color:#111}
.text{font-size:11px;color:var(--grey);line-height:13.5px}

.categories{left:20px;top:706px;width:389px;height:112px;background:#eef7fd;border:2px solid #a9d6f1}
.categories ul{position:absolute;list-style:none;top:11px;color:var(--link);font-size:11px;line-height:17px}

.jobs{left:20px;top:824px;width:390px;height:174px;border:2px solid #a9d6f1;border-top:0}
.jobs table{width:100%;border-collapse:collapse;font-size:11px}
.jobs th{background:var(--blue);color:#fff;font-weight:400;font-size:13px;text-align:left;height:22px;padding-left:16px}
.jobs td{height:18.7px;padding-left:12px;color:#222}
.jobs tr:nth-child(even) td{background:#f1f1f1}
.jobs td.co{color:var(--link);background:#fafcfe}
.jobs td.loc{color:var(--link);background:#eaeaea}

.news{left:415px;top:177px;width:252px;height:236px}
.news .item{padding:0 14px;margin-top:10px}
.news .date{color:#222}
.alert{left:415px;top:414px;width:252px;height:82px;background:linear-gradient(#1ea0ea,#0b7fcf);color:#fff;padding:18px 0 0 20px}
.alert-title{font-size:22px;line-height:1}
.alert-sub{font-size:13px;opacity:.9}
.go{position:absolute;right:30px;top:26px;width:28px;height:28px;border-radius:50%;background:#111;border:2px solid #fff;font-size:13px;display:flex;align-items:center;justify-content:center}
.why{left:415px;top:497px;width:252px;height:218px}
.why h3{font-size:14px;font-weight:400;color:#111;padding:15px 0 0 12px}
.tag{position:absolute;left:1px;width:124px;height:18px;background:var(--yellow);font-size:13px;padding-left:14px;color:#222}
.why ul{position:absolute;left:20px;list-style:none;font-size:11px;color:#333;line-height:17.5px}
.why li::before{content:"▸ ";font-size:9px}
.why-photo{position:absolute;right:1px;top:30px;width:120px;height:186px;background:linear-gradient(#f1f1f1,#c9ccd3 55%,#26272c)}

.partners{left:420px;top:797px;width:232px;height:204px;border:6px solid var(--blue)}
.badge{position:absolute;width:96px;height:28px;border:1px solid #a9c5dd}

.post{left:672px;top:177px;width:168px;height:85px;background:var(--orange);color:#fff;padding:10px 0 0 17px}
.post-title{font-size:21px;font-weight:600;line-height:24px;letter-spacing:.5px}
.post-sub{font-size:12px;opacity:.9}
.login{left:672px;top:269px;width:170px;height:134px}
.login .head{height:26px;background:linear-gradient(#fff,#e7e7e7);font-size:14px;padding:4px 11px;color:#111}
.map{left:672px;top:409px;width:170px;height:116px;background:linear-gradient(135deg,#f7c31d,#e9a90d);border:1px solid #bcd}
.sresume{left:672px;top:532px;width:171px;height:80px;background:var(--blue);color:#fff;padding:9px 11px}
.grads{left:672px;top:619px;width:172px;height:150px;padding:6px 11px}
.social{top:810px;width:52px;height:48px;display:flex;align-items:center;justify-content:center;font-size:10px;font-weight:600;color:#fff}

.footer{left:0;top:1025px;width:868px;height:122px;background:var(--footer);color:#fff;padding:17px 34px}
.footer h4{font-size:16px;font-weight:400}
.footer nav{margin-top:7px;font-size:10px;color:#d6e6f3}
.footer nav span{margin:0 5px;opacity:.7}
.bottombar{left:0;top:1147px;width:868px;height:53px;background:var(--footer-dark);color:#fff;font-size:10px;text-align:right;padding:8px 40px 0 0;line-height:16px}
</style>
</head>
<body>

<div class="abs topbar">Jobs on Mobile &nbsp;|&nbsp; Jobs by Email</div>

<header>
  <div class="abs brand">
    <div class="brand-name">Wendholt</div>
    <div class="brand-tag">your punch lines goes here</div>
  </div>
  <div class="abs promo">
    <div class="promo-q">IS YOUR<br>RESUME ‘READY’<br>TO GET YOU NOTICED?</div>
    <div class="promo-seal">Special<br>Offer<br>Price</div>
    <div class="promo-cta">GET IT ANALYSED BY RESUME EXPERTS</div>
  </div>
</header>

<nav class="abs nav">
  <a>Home</a><a class="active">Jobs</a><a>Account</a><a>Register</a><a>News &amp; Insight</a><a>Graduates</a><a>Recruiters</a><a>About Us</a><a>Contact Us</a>
</nav>
<div class="abs subnav">Advanced Job Search &nbsp; | &nbsp; Companies</div>

<!-- Left column -->
<section class="abs box signin">
  <div class="head-yellow"><svg width="18" height="16" viewBox="0 0 18 16"><path d="M2 8l5 5L16 2" fill="none" stroke="#fff" stroke-width="3"/></svg>SIGN IN</div>
  <div class="abs label" style="left:18px;top:37px">Username</div>
  <div class="abs label" style="left:191px;top:35px">Password</div>
  <div class="abs field" style="left:17px;top:57px;width:157px">type your username</div>
  <div class="abs field" style="left:191px;top:57px;width:160px">******************</div>
  <div class="abs btn" style="left:17px;top:85px;width:83px;height:24px;font-size:14px;text-align:center;padding-top:2px">Sign In</div>
  <div class="abs" style="left:17px;top:118px;font-size:11px"><span class="check"></span>keep me signed in</div>
  <div class="abs" style="left:18px;top:134px;font-size:11px;text-decoration:underline;color:#222">Forget Your Password</div>
</section>

<section class="abs quick">
  <div class="head-black">Quick Search</div>
  <div class="label" style="top:41px">Keyword</div>
  <div class="abs field" style="left:80px;top:42px;width:275px">type your keyword here</div>
  <div class="label" style="top:69px">Location</div>
  <div class="abs field" style="left:80px;top:69px;width:275px">City, State, Zip code</div>
  <div class="abs" style="left:17px;top:98px;font-size:11px;color:#333"><span class="check"></span>Contract &nbsp;&nbsp; <span class="check"></span>Permanent</div>
  <div class="abs" style="left:16px;top:123px;width:93px;height:22px;background:#14253a;color:#fff;font-size:12px;padding:3px 6px">SEARCH NOW</div>
  <div class="abs" style="left:18px;top:157px;font-size:11px;color:#333;text-decoration:underline">Advanced Search</div>
  <svg class="abs" style="left:101px;top:159px" width="16" height="10" viewBox="0 0 16 10"><path d="M0 5h13M9 1l4 4-4 4" fill="none" stroke="#e08a00" stroke-width="1.6"/></svg>
  <div class="abs field" style="left:122px;top:156px;width:227px"></div>
</section>

<section class="abs" style="left:21px;top:553px;width:380px">
  <h2 class="section">Welcome Note</h2>
  <p class="text" style="margin-top:4px">Crystalline eSolutions is a web service company, offering a wide range of services which range from designing and development, that is covering almost all the fields in the best possible way. To be the best we know what and how to present beautifully the working of the client’s need and their advantages be highlighted.</p>
  <p class="text" style="margin-top:8px">The only way to success is through the right path and that’s what we provide you. None of the other companies has the result we do.</p>
</section>

<h2 class="abs section" style="left:22px;top:679px">Job Category</h2>
<section class="abs categories">
  <ul style="left:15px"><li>Accounting (30)</li><li>IT Software jobs (100)</li><li>BPO jobs (50)</li><li>Sales jobs (60)</li><li>Sales Manager (50)</li></ul>
  <ul style="left:134px"><li>Managment (30)</li><li>Hotel Managment (80)</li><li>BPO jobs (50)</li><li>Finance jobs (15)</li><li>Computers (10)</li></ul>
  <ul style="left:266px;top:8px"><li>Web Designing (30)</li><li>Consultants (100)</li><li>BPO jobs (50)</li><li>Sales jobs (60)</li><li>Multemedia (15)</li></ul>
</section>

<section class="abs jobs">
  <table>
    <tr><th style="width:138px">Job Title</th><th style="width:125px;padding-left:12px">Company</th><th style="padding-left:24px">Location</th></tr>
    <tr><td>Office Receptionist</td><td class="co">Tester LTD</td><td class="loc">New Delhi</td></tr>
    <tr><td>Web Designer</td><td class="co">Tarn Moto</td><td class="loc">Florida</td></tr>
    <tr><td>Web Developer</td><td class="co">Relmont</td><td class="loc">&nbsp;New Delhi</td></tr>
    <tr><td>Credit Analyst</td><td class="co">Sunleaf Web Services</td><td class="loc">Madras</td></tr>
    <tr><td>Service Senior Manger</td><td class="co">Helix Info Sys</td><td class="loc">Noida, UP</td></tr>
    <tr><td>Sales Manager</td><td class="co">Microvale Corp.</td><td class="loc">New Delhi</td></tr>
    <tr><td>Computer Operator</td><td class="co">Oldbury</td><td class="loc">Okhla</td></tr>
    <tr><td>Senior Accountant</td><td class="co">MaterWeb Corp.</td><td class="loc">Mumbai</td></tr>
  </table>
</section>

<!-- Middle column -->
<section class="abs box news">
  <div class="head-yellow"><svg width="18" height="16" viewBox="0 0 18 16"><path d="M2 8l5 5L16 2" fill="none" stroke="#fff" stroke-width="3"/></svg>Latest News &amp; Insight</div>
  <div class="item"><div class="date">20.11.2011</div><div class="text">To manage the static website HTML knowledge is the required. The simple website</div></div>
  <div class="item"><div class="date">15.11.2011</div><div class="text">Static website is a simple way to get your message out to the public.</div></div>
  <div class="item"><div class="date">12.11.2011</div><div class="text">We believe that you need us to represent beautifully the unique</div></div>
  <div class="item" style="text-decoration:underline;color:#222">More Articles</div>
</section>

<section class="abs alert">
  <div class="alert-title">EMAIL JOB ALERT</div>
  <div class="alert-sub">NOW JOB ALERT ON EMAIL</div>
  <div class="go">Go</div>
</section>

<section class="abs box why">
  <h3>Why RolesForMetrics?”</h3>
  <div class="tag" style="top:48px">Jobseekers</div>
  <ul style="top:68px"><li>your job subline</li><li>Find jobs now</li><li>Get joby by emial or</li></ul>
  <div class="tag" style="top:130px">Recruiters</div>
  <ul style="top:150px"><li>Get Rusume Update Now</li><li>Find your dream job here</li><li>Get joby by emial</li></ul>
  <div class="why-photo" role="img" aria-label="Photo of a smiling businesswoman in a dark suit gesturing with an open hand"></div>
</section>

<h2 class="abs section" style="left:420px;top:736px">Featured Partners</h2>
<p class="abs text" style="left:420px;top:762px;width:245px">The only way to success is through the right path and that’s what we provide you. None of the other com-</p>
<section class="abs partners" aria-label="Partner badges">
  <div class="badge" style="left:5px;top:1px;background:#fff"></div>
  <div class="badge" style="left:113px;top:1px;background:#fff"></div>
  <div class="badge" style="left:5px;top:33px;background:#1a7a2a"></div>
  <div class="badge" style="left:113px;top:33px;background:#fff"></div>
  <div class="badge" style="left:5px;top:64px;background:#eef3fa"></div>
  <div class="badge" style="left:113px;top:64px;background:#fff"></div>
  <div class="badge" style="left:5px;top:96px;background:#fff"></div>
  <div class="badge" style="left:113px;top:96px;background:#e51b23"></div>
  <div class="badge" style="left:5px;top:127px;background:#fff"></div>
  <div class="badge" style="left:113px;top:127px;background:#2f5fa7"></div>
  <div class="badge" style="left:5px;top:158px;height:30px;background:#d8141c"></div>
</section>

<!-- Right column -->
<section class="abs post">
  <div class="post-title">POST YOUR<br>RESUME »</div>
  <div class="post-sub">click here to post now</div>
</section>

<section class="abs box login">
  <div class="head">Log In</div>
  <div class="abs" style="left:10px;top:35px">Email Id</div>
  <div class="abs field" style="left:10px;top:49px;width:147px;height:16px"></div>
  <div class="abs" style="left:10px;top:70px">Password</div>
  <div class="abs field" style="left:10px;top:84px;width:147px;height:16px"></div>
  <div class="abs btn" style="left:10px;top:106px;width:52px;height:17px;font-size:11px;text-align:center;padding-top:1px">LOG IN</div>
</section>

<div class="abs map" role="img" aria-label="Map of the United States with states in yellow"></div>

<section class="abs sresume">
  <div style="font-size:14px">Search resume</div>
  <div class="abs field" style="left:11px;top:30px;width:126px;height:18px;border:0">type here your resume</div>
  <div class="abs" style="left:137px;top:30px;width:25px;height:18px;background:#fff;border-left:1px solid #ccc">
    <svg width="25" height="18" viewBox="0 0 25 18"><circle cx="10" cy="8" r="4.5" fill="none" stroke="#111" stroke-width="2"/><path d="M13.5 11.5l5 4" stroke="#111" stroke-width="2.5"/></svg>
  </div>
</section>

<section class="abs box grads">
  <div style="font-size:13px;color:#111">Graduates</div>
  <p class="text" style="margin-top:4px;line-height:12.5px">Static website is a simple way to get your message out to the public. Static website are cheaper and also it needs less maintenance too.</p>
  <p class="text" style="margin-top:8px;line-height:12.5px">It’s the simplest, cheapest and also the basic thing the search engine picks it up very easily. We</p>
</section>

<div class="abs social" style="left:695px;background:#3fa9e8">Chirpline</div>
<div class="abs social" style="left:767px;width:48px;background:#f28a1c">Feedwire</div>

<footer class="abs footer">
  <h4>Useful Links</h4>
  <nav>Home<span>|</span>Jobs<span>|</span>Account<span>|</span>Register<span>|</span>News &amp; Insight<span>|</span>Graduates<span>|</span>Recruiters<span>|</span>About Us<span>|</span>Contact Us</nav>
</footer>
<div class="abs bottombar">copyright © 2011 company name &nbsp;All right reserved<br>Tems &amp; conditions</div>

</body>
</html>
```